Website for a financial survey consultancy

WHO WE ARE
We're a niche HR consultancy specialising in salary comparison surveys for the financial asset management industry. We position ourselves as a small, highly responsive organisation with a strong personal relationship with each of our 50+ blue-chip clients.

WHAT WE DO
Our business is 80% surveys (= products), 20% consultancy (= services). The surveys are a set of online products which clients interact with to find the information they are interested in.

WHAT WE WANT
We are completely revising our existing marketing website and need a new up-to-date look and feel for the site. We want you to design 2 web pages
- Home page
- Internal content page

More details below in Must Have Priorities.

REFERENCE SITES
- www.tallowmere.com - nice background image
- www.quimbelt.com - ignoring the animations
- www.palvastro.com
- www.dulmiko.com - clean, fresh, styly but prob not corporate enough
- www.orvettagrove.com - spacious, beautiful, slightly dated tho
- www.plinzer.co.uk - ignore the colours. Like the simplicity, larger font size (although want to stick with sans-serif fonts for main content)

DELIVERABLES
The final designs should be delivered as one or more PSD files with clearly named layers. All design elements and treatments should be separated out, for example use adjustment layers rather than applied (and subsequently irreversible) adjustments, strokes, shading, etc.

WHAT NEXT
I'll be monitoring the contest every day and can respond to questions fast. You can IM me on Skype or MSN.

Reason: Hi folks,

I am extending the deadline to this project as I am travelling this week and therefore will not be able to make a final decision until next Monday. I will try and provide further feedback over the course of this week but I am only going to be online occasionally so be prepared to wait a few days for a reply from me.

Thanks for all the designs so far.

Owen

Target Market(s)

In order of importance, most important first

1. Potential customers - UK & US financial industry HR professionals, short on time. Heard about us already, want to find out more about what we do, confirm relevance for their needs. Core goal - establish credibility: are we properly resourced, will we be around for years to come, are we *real*.

2. Existing customers - UK & US financial industry professionals, short on time, under pressure, want results quickly, minimum faff, expect high quality, slickly presented information. Primary action: login and use surveys.

3. Industry professionals/researchers - probably arriving through blog content, looking to browse and hoover information. Valuable for their ability to spread awareness of who we are amongst their peers.

Industry/Entity Type

Financial

Requirements
Must have
• GENERAL
Style cues - Corporate, professional, financial, stylish, slick, clean, spacious, light
Size - standard 960px grid

NAVIGATION
- [ Home | About us | Surveys | Consulting | Blog ]
- Sub-nav (roll-over dropdown) on About Us, Surveys & Consulting

ALL PAGES
- Site navigation
- Client login (on screen permanently or link to ajaxy in-page pop-up)
- Footer section
- Existing logo (attached)* - this is obviously an important reference point in the design, esp colour

HOME PAGE
- Communicate (link thru to?) survey/consulting split
- Large photo(s)/backdrop (2-3 interchangeable options ideally). Please consider what rights agreement will be necessary for any photos you include in your design.
- Possibly bigger more prominent version of logo
- Strap line/sentence - "Focussed data is the key to success"
- 3 recent blog posts (should look good with and without blog post images)
- Free downloadable PDF research report + supporting blurb

INTERNAL PAGE
- Page title
- Content - typical page will be less than one screenfull
- Level 1 sub-heading
- Level 2 sub-heading
- Bulleted list
- Content supporting image (any image will do - interested in placement, borders (if any), spacing, caption, etc)
- 'Do something' button

* Note: there is some internal debate about this logo at the moment. Some (me) are keen for it to change, some (not me!) are not. If you have an web page design idea/concept that requires an evolution of the logo, go ahead and evolve it. We can explore this further in the design process as necessary, but don't sweat it.
Nice to have
• Values to communicate
- Knowledgeable
- Professional
- Secure
- Personal
- Experienced
- Financial industry specific
- Accurate
- Reliable
Should not have
• - Search box
- Social media links, other than RSS feed button (discrete)

```html
<!DOCTYPE html>
<html lang="en">
<head>
<meta charset="utf-8">
<title>Corvane — Financial Survey Consultancy</title>
<link href="https://fonts.googleapis.com/css2?family=Questrial&family=Arimo:wght@400;700&family=Tinos:wght@700&display=swap" rel="stylesheet">
<style>
  :root{
    --maroon:#7b1115;
    --red:#a01318;
    --ink:#111;
    --dark:#29251e;
    --bar:#27241f;
    --muted:#b9b6ae;
    --line:#3d3930;
    --card-top:#ffffff;
    --card-bottom:#e3e4e6;
  }
  *{box-sizing:border-box;margin:0;padding:0}
  html,body{width:1200px;height:799px;overflow:hidden}
  body{
    position:relative;
    font-family:'Arimo',Arial,sans-serif;
    background:var(--dark);
  }
  .masthead{
    position:absolute;left:0;top:0;width:1200px;height:465px;
    background:radial-gradient(ellipse 700px 320px at 62% 10%,#fbfaf8 0%,#efece6 55%,#d8d5cf 100%);
  }
  .brand{
    position:absolute;left:138px;top:10px;width:117px;height:112px;
    background:var(--maroon);
    box-shadow:5px 4px 0 #c98d91;
    display:flex;align-items:center;justify-content:center;
    color:#fff;font-weight:700;font-size:20px;
  }
  .client-login{
    position:absolute;left:939px;top:34px;width:114px;height:25px;
    background:#5f5a57;border-radius:4px;padding:4px;
  }
  .client-login a{
    display:flex;align-items:center;gap:8px;height:100%;
    background:var(--maroon);border:1px solid #e6d0d0;
    color:#fff;font-size:11px;text-decoration:none;padding-left:8px;
  }
  .client-login svg{width:5px;height:6px}
  .main-nav{position:absolute;top:83px;left:0;width:1200px;height:28px}
  .main-nav a{
    position:absolute;top:0;height:28px;line-height:28px;
    font-family:'Questrial',sans-serif;font-size:18px;color:var(--maroon);
    text-decoration:none;transform:translateX(-50%);white-space:nowrap;
  }
  .main-nav a.current{
    width:79px;text-align:center;background:var(--red);color:#fff;border-radius:4px;
  }
  .hero{
    position:absolute;left:138px;top:125px;width:915px;height:340px;
    border-radius:4px 4px 0 0;overflow:hidden;
  }
  .hero-photo{
    position:absolute;inset:0;
    background:linear-gradient(100deg,#3a3530 0%,#d8d3cd 28%,#e6e9ee 48%,#b9c7d6 70%,#dfe7ef 100%);
  }
  .hero-title{
    position:absolute;left:447px;top:44px;width:430px;
    font-family:'Tinos',Georgia,serif;font-weight:700;font-size:44px;line-height:47px;
    color:var(--red);letter-spacing:-0.5px;
  }
  .hero-blurb{
    position:absolute;left:445px;top:171px;width:447px;height:79px;
    background:rgba(235,236,238,.82);border-radius:4px;
    padding:9px 6px;font-size:15px;line-height:21px;color:var(--ink);
  }
  .slide-pager{position:absolute;left:11px;top:307px;display:flex;gap:3px}
  .slide-pager span{
    width:20px;height:20px;border-radius:3px;background:#fff;color:#a9a9a9;
    font-family:'Tinos',Georgia,serif;font-weight:700;font-size:16px;
    display:flex;align-items:center;justify-content:center;
  }
  .slide-pager span.active{background:var(--red);color:#fff}
  .section-nav{
    position:absolute;left:591px;top:302px;width:324px;height:38px;
    background:var(--bar);
  }
  .section-nav a{color:#fff;font-weight:700;font-size:13.5px;text-decoration:none;position:absolute;top:12px}
  .section-nav .notch{position:absolute;left:50px;top:-6px}
  .card{
    position:absolute;top:503px;height:144px;border-radius:5px;
    background:linear-gradient(var(--card-top) 35%,var(--card-bottom));
    border:1px solid #8d8a86;
  }
  .intro{left:138px;width:597px;padding:13px 21px}
  .intro h2{font-size:15px;font-weight:700;color:var(--ink);margin-bottom:8px}
  .intro p{font-size:11px;line-height:17.5px;color:var(--ink)}
  .intro p strong{font-size:12.5px}
  .intro .read-more{
    position:absolute;right:29px;bottom:20px;font-weight:700;font-size:12px;color:var(--ink);text-decoration:none;
  }
  .latest-blogs{left:792px;width:261px;padding:16px 22px 0 23px}
  .latest-blogs h3{
    font-family:'Tinos',Georgia,serif;font-weight:700;font-size:15px;color:var(--maroon);margin-bottom:1px;
  }
  .latest-blogs p{font-size:10.5px;line-height:14px;color:var(--ink)}
  .latest-blogs hr{border:0;border-top:1px dotted #555;width:180px;margin:2px 0 4px}
  .latest-blogs .read-all{
    position:absolute;right:23px;bottom:10px;font-size:11px;color:var(--ink);
  }
  .site-footer{position:absolute;left:0;top:698px;width:1200px;height:101px}
  .footer-col{
    position:absolute;top:0;font-size:11px;line-height:15.5px;color:var(--muted);
  }
  .footer-col strong{color:#d2cfc8}
  .footer-divider{position:absolute;top:2px;width:1px;height:80px;background:var(--line)}
  .social{position:absolute;left:901px;top:44px;display:flex;gap:11px}
  .social span{width:30px;height:28px;border-radius:5px;background:#48433d}
  .copyright{
    position:absolute;right:147px;top:80px;font-size:9.5px;color:var(--muted);letter-spacing:.3px;
  }
</style>
</head>
<body>
  <header class="masthead">
    <div class="brand">Corvane</div>
    <div class="client-login">
      <a href="#"><svg viewBox="0 0 5 6"><path d="M0 0L5 3L0 6Z" fill="#fff"/></svg>Client Login</a>
    </div>
    <nav class="main-nav">
      <a class="current" href="#" style="left:543px">Home</a>
      <a href="#" style="left:654px">About us</a>
      <a href="#" style="left:769px">Surveys</a>
      <a href="#" style="left:891px">Consulting</a>
      <a href="#" style="left:1000px">Blog</a>
    </nav>
    <section class="hero">
      <div class="hero-photo" role="img" aria-label="Photo of three smiling colleagues working together at a computer in a bright office"></div>
      <h1 class="hero-title">Focussed data is the key to success</h1>
      <p class="hero-blurb">It is a long established fact that a reader will be distracted by the readable content of a page when looking at its layout. The point of using Lorem Ipsum is that i</p>
      <div class="slide-pager"><span class="active">1</span><span>2</span><span>3</span></div>
      <nav class="section-nav">
        <svg class="notch" width="12" height="6" viewBox="0 0 12 6"><path d="M0 6L6 0L12 6Z" fill="#27241f"/></svg>
        <a href="#" style="left:25px">About Us</a>
        <a href="#" style="left:130px">Surveys</a>
        <a href="#" style="left:227px">Consulting</a>
      </nav>
    </section>
  </header>

  <article class="card intro">
    <h2>financial survey consultancy</h2>
    <p><strong>It is a long established fact that a reader will be distracted by</strong> the readable content of a page when looking at its layout. The point of using Lorem Ipsum is that ilt is a long established fact that a reader will be distracted by the readable content of a page when looking at its layout. The point of using Lorem Ipsum is that i</p>
    <a class="read-more" href="#">Read More</a>
  </article>

  <aside class="card latest-blogs">
    <h3>Latest Blogs</h3>
    <p>fact that a reader will be distracted by the readable fact that a reader will be dis-tracted</p>
    <hr>
    <p>fact that a reader will be distracted by the readable fact that a reader will be dis-tracted ...</p>
    <a class="read-all" href="#">Read All</a>
  </aside>

  <footer class="site-footer">
    <div class="footer-col" style="left:139px">
      <strong>Bramley Office</strong><br>48 Elmcourt Rd. Suite 210<br>Fenwick, CA 2460<br>t: 555.014.2268<br>f: 555.014.3391
    </div>
    <div class="footer-divider" style="left:285px"></div>
    <div class="footer-col" style="left:326px">
      <strong>Bramley Office</strong><br>48 Elmcourt Rd. Suite 210<br>Fenwick, CA 2460<br>t: 555.014.2268<br>f: 555.014.3391
    </div>
    <div class="footer-divider" style="left:478px"></div>
    <div class="footer-col" style="left:517px">Site Map<br>Careers<br>Press<br>Blog</div>
    <div class="social" aria-label="Social links"><span></span><span></span><span></span><span></span></div>
    <p class="copyright">Copyright © 2010, Corvane. All rights reserved.</p>
  </footer>
</body>
</html>
```